Corvane Industries business cards

We need business cards for our company Corvane Industries, based in Brisbane but trading world wide. We buy and sell Corvane Industries, generators and marine equipment. The design needs to be kept clean, simple but eye catching.
Please keep with our current logo (included) and further information can be included on request

Business

0792cd
33a6d7
85cae6
3276b5
0455a3
cedeed
cee9f5
ffffff

```html
<!DOCTYPE html>
<html lang="en">
<head>
<meta charset="utf-8">
<title>Corvane Industries – Business Card</title>
<link href="https://fonts.googleapis.com/css2?family=Roboto:wght@400;700&display=swap" rel="stylesheet">
<style>
  :root {
    --deep-blue: #0455a3;
    --brand-blue: #3276b5;
    --mid-blue: #33a6d7;
    --bright-blue: #0792cd;
    --soft-blue: #85cae6;
    --pale-blue: #cee9f5;
    --mist: #cedeed;
    --white: #ffffff;
    --ink: #555a60;
    --backdrop: #eef1f4;
  }
  * { margin: 0; padding: 0; box-sizing: border-box; }
  html, body {
    width: 1200px; height: 1023px; overflow: hidden;
    background: var(--backdrop);
    font-family: "Roboto", Arial, sans-serif;
  }
  .card {
    position: absolute; left: 120px; top: 231px;
    width: 960px; height: 560px;
    background: linear-gradient(135deg, var(--white) 0%, #f4f6f8 100%);
    border-radius: 36px;
    box-shadow: 0 6px 24px rgba(40, 60, 90, 0.18);
    overflow: hidden;
  }
  .beams { position: absolute; inset: 0; }
  .brand { position: absolute; left: 70px; top: 120px; }
  .brand-square {
    width: 190px; height: 190px; border-radius: 28px;
    background: linear-gradient(135deg, var(--brand-blue), var(--mid-blue));
  }
  .brand-name {
    margin-top: 22px;
    font-weight: 700; font-size: 62px; line-height: 0.95;
    color: var(--mid-blue); letter-spacing: -1px;
  }
  .contact {
    position: absolute; right: 70px; top: 68px;
    text-align: right; color: var(--ink);
    font-size: 19px; line-height: 27px;
  }
  .person { font-size: 26px; margin-bottom: 14px; }
  .person-name { color: var(--mid-blue); font-weight: 700; }
  .person-role { color: var(--ink); font-size: 18px; }
  .divider { color: var(--soft-blue); margin: 0 6px; }
  .line { display: flex; justify-content: flex-end; align-items: center; gap: 10px; }
  .icon {
    width: 17px; height: 17px; border-radius: 4px;
    background: var(--bright-blue); display: inline-block;
  }
  .icon svg { display: block; }
  .company { margin-top: 22px; color: var(--mid-blue); font-weight: 700; }
</style>
</head>
<body>
  <section class="card">
    <svg class="beams" width="960" height="560" viewBox="0 0 960 560" aria-hidden="true">
      <polygon points="960,0 780,0 520,560 700,560" fill="var(--pale-blue)" opacity="0.45"/>
      <polygon points="960,40 960,200 420,560 300,560" fill="var(--pale-blue)" opacity="0.35"/>
    </svg>

    <div class="brand">
      <div class="brand-square"></div>
      <div class="brand-name">Corvane<br>Industries</div>
    </div>

    <div class="contact">
      <div class="person"><span class="person-name">Maren Tollby</span><span class="divider">|</span><span class="person-role">Director</span></div>
      <div class="line">+61 7 3000 4182 <span class="icon"><svg width="17" height="17" viewBox="0 0 17 17"><path d="M5 4l2 2-1 1.5c.8 1.6 1.9 2.7 3.5 3.5L11 10l2 2-1.5 1.5C7.5 13 4 9.5 3.5 5.5z" fill="#fff"/></svg></span></div>
      <div class="line">+61 400 552 917 <span class="icon"><svg width="17" height="17" viewBox="0 0 17 17"><rect x="6" y="3" width="5" height="11" rx="1" fill="#fff"/></svg></span></div>
      <div class="line">+61 7 3000 7265 <span class="icon"><svg width="17" height="17" viewBox="0 0 17 17"><rect x="4" y="5" width="9" height="7" rx="1" fill="#fff"/></svg></span></div>
      <div class="line">maren@corvane-ind.com.au <span class="icon"><svg width="17" height="17" viewBox="0 0 17 17"><path d="M3 5h11v7H3z M3 5l5.5 4L14 5" fill="none" stroke="#fff" stroke-width="1.4"/></svg></span></div>
      <div class="line">www.corvane-ind.com.au <span class="icon"><svg width="17" height="17" viewBox="0 0 17 17"><circle cx="8.5" cy="8.5" r="5" fill="none" stroke="#fff" stroke-width="1.4"/><path d="M3.5 8.5h10" stroke="#fff" stroke-width="1.2"/></svg></span></div>
      <div class="company">Corvane Industries Pty Ltd</div>
      <div class="line">14 Kestrel Lane, Hemmant QLD 4174</div>
      <div class="line">PO Box 582, Tingalpa QLD 4173</div>
    </div>
  </section>
</body>
</html>
```